Fizz Bop Lantern Series 1 Volume 1

I am looking for someone to make me a book cover, I want something catchy but classy.

The title of the book is; Fizz Bop Lantern
Series 1 Volume 1

Colors should be: Red, White, Black and Grey

```html
<!DOCTYPE html>
<html lang="en">
<head>
<meta charset="utf-8">
<title>Fizz Bop Lantern – Series 1 Volume 1</title>
<link rel="stylesheet" href="https://fonts.googleapis.com/css2?family=Poppins:wght@800&family=Oswald:wght@500&family=Montserrat:wght@700&display=swap">
<style>
  :root {
    --stage: #0b0b0b;
    --paper: #f4f4f4;
    --paper-edge: #e6e6e6;
    --ink: #111111;
    --red: #e8202a;
    --navy: #1b3a8c;
    --white: #ffffff;
    --grey-light: #f1f1f1;
    --grey-mid: #d9d9d9;
  }
  * { margin: 0; padding: 0; box-sizing: border-box; }
  html, body {
    width: 1200px;
    height: 843px;
    overflow: hidden;
    background: var(--stage);
  }
  .canvas {
    position: relative;
    width: 1200px;
    height: 843px;
  }
  .cover {
    position: absolute;
    left: 319px;
    top: 26px;
    width: 562px;
    height: 792px;
    background: linear-gradient(90deg, var(--paper-edge) 0%, var(--paper) 4%, var(--white) 50%, var(--paper) 100%);
    overflow: hidden;
  }
  .volume-tag {
    position: absolute;
    left: 129px;
    top: 21px;
    width: 306px;
    height: 39px;
    border: 2px solid var(--red);
    display: flex;
    align-items: center;
    justify-content: center;
    font-family: 'Oswald', sans-serif;
    font-weight: 500;
    font-size: 27px;
    letter-spacing: 13px;
    padding-left: 13px;
    color: var(--ink);
  }
  .title {
    position: absolute;
    left: 0;
    width: 100%;
    text-align: center;
    font-family: 'Poppins', sans-serif;
    font-weight: 800;
    line-height: 1;
  }
  .title-top {
    top: 80px;
    font-size: 68px;
    letter-spacing: 4px;
    color: var(--ink);
  }
  .title-top .accent { color: var(--red); }
  .title-bottom {
    top: 148px;
    font-size: 84px;
    letter-spacing: 3px;
    color: var(--red);
  }
  .series-tag {
    position: absolute;
    left: 174px;
    top: 252px;
    width: 213px;
    height: 34px;
    background: var(--navy);
    display: flex;
    align-items: center;
    justify-content: center;
    font-family: 'Oswald', sans-serif;
    font-weight: 500;
    font-size: 22px;
    letter-spacing: 9px;
    padding-left: 9px;
    color: var(--white);
  }
  .stacked-binders {
    position: absolute;
    left: 68px;
    top: 321px;
    width: 432px;
    height: 320px;
    background: linear-gradient(180deg, #f2a900 0%, #e2242b 30%, #1f5a3a 60%, #1f3fa0 88%, #e9e9e9 100%);
    border-radius: 4px;
  }
  .author-band {
    position: absolute;
    left: 0;
    top: 731px;
    width: 100%;
    height: 46px;
    background: var(--red);
    display: flex;
    align-items: center;
    justify-content: center;
    font-family: 'Montserrat', sans-serif;
    font-weight: 700;
    font-size: 23px;
    letter-spacing: 3px;
    color: var(--white);
  }
</style>
</head>
<body>
<div class="canvas">
  <div class="cover">
    <div class="volume-tag">VOLUME-1</div>
    <h1 class="title title-top">FIZZ B<span class="accent">O</span>P</h1>
    <h2 class="title title-bottom">LANTERN</h2>
    <div class="series-tag">SERIES-1</div>
    <div class="stacked-binders" role="img" aria-label="Photo of four stacked office ring binders in yellow, red, green and blue with a soft reflection"></div>
    <div class="author-band">MARLA JEAN TOFIELD</div>
  </div>
</div>
</body>
</html>
```